Leap! Maximizing the Transfer of a Company to Seasoned Buyers

We are a private equity firm, and the partners wrote this book to help business owners understand the process for selling their business. We need a cover for the book, and our current thinking is a picture of a person (or just the leg/foot w/business shoe) walking out a door, representing our title "Leap!"
Business owners will benefit from learning what professional investors, like private equity firms, are looking for and how the process is likely to unfold. Business owners will also learn how to prepare their company and themselves for this process.

Target Market(s)

Small to medium sized business owners

Font styles to use
Serif

Colors
3277b5
3276b5
85acd3
cfdeed

Requirements
Must have
• a professional look and feel that will attract business owners and a compelling call to action for those business owners considering a sale of their business
Nice to have
• Leverage the same color blue and possibly logo from Birch Hollow Capital, which can be seen here - https://birchhollowcap.example/
Should not have
• humor/quirkiness/schtick

```html
<!DOCTYPE html>
<html lang="en">
<head>
<meta charset="utf-8">
<title>Leap! Maximizing the Transfer of a Company to Seasoned Buyers</title>
<link rel="stylesheet" href="https://fonts.googleapis.com/css2?family=Oswald:wght@400;500&display=swap">
<style>
  :root {
    --cover-blue: #4470b2;
    --scene-blue: #4d7ec0;
    --scene-mid: #8fb0dc;
    --path-white: #ffffff;
    --title-white: #ffffff;
    --title-shadow: #2a1a52;
    --band-white: #ffffff;
    --brand-navy: #1f2b5a;
  }
  html, body {
    margin: 0;
    padding: 0;
    overflow: hidden;
    background: var(--cover-blue);
  }
  .cover {
    position: relative;
    width: 800px;
    height: 1200px;
    overflow: hidden;
    background: var(--cover-blue);
  }
  .scene-art {
    position: absolute;
    left: 0;
    top: 480px;
    width: 800px;
    height: 619px;
    background: linear-gradient(51deg,
      var(--scene-blue) 0%,
      var(--scene-blue) 45%,
      var(--scene-mid) 47%,
      var(--path-white) 50%,
      var(--path-white) 68%,
      var(--scene-mid) 78%,
      var(--scene-blue) 88%,
      var(--scene-blue) 100%);
  }
  .cover-title {
    position: absolute;
    left: 0;
    top: 0;
    width: 800px;
    height: 470px;
  }
  .cover-title text {
    font-family: "Oswald", sans-serif;
    font-weight: 400;
    font-size: 483px;
  }
  .title-shadow { fill: var(--title-shadow); }
  .title-face { fill: var(--title-white); }
  .cover-subtitle {
    position: absolute;
    left: 79px;
    top: 828px;
    margin: 0;
    font-family: "Oswald", sans-serif;
    font-weight: 500;
    font-size: 44px;
    line-height: 52px;
    letter-spacing: -0.5px;
    color: var(--title-white);
  }
  .brand-band {
    position: absolute;
    left: 0;
    top: 1099px;
    width: 800px;
    height: 101px;
    background: var(--band-white);
    display: flex;
    align-items: center;
    justify-content: center;
    gap: 18px;
  }
  .brand-mark {
    width: 44px;
    height: 44px;
    background: var(--brand-navy);
  }
  .brand-name {
    font-family: "Oswald", sans-serif;
    font-weight: 400;
    font-size: 44px;
    color: var(--brand-navy);
    letter-spacing: 0.5px;
  }
</style>
</head>
<body>
  <main class="cover">
    <div class="scene-art" role="img" aria-label="Illustration: a businessman with a briefcase stands on a white lit path leading to a distant open doorway, a pink arrow at his feet pointing toward the door"></div>

    <svg class="cover-title" viewBox="0 0 800 470" aria-label="Leap!">
      <text class="title-shadow" x="88" y="453" textLength="632" lengthAdjust="spacingAndGlyphs">Leap!</text>
      <text class="title-face" x="84" y="449" textLength="632" lengthAdjust="spacingAndGlyphs">Leap!</text>
    </svg>

    <p class="cover-subtitle">How to prepare<br>your company and<br>yourselves for<br>selling your business!</p>

    <footer class="brand-band">
      <span class="brand-mark"></span>
      <span class="brand-name">Birch Hollow Capital</span>
    </footer>
  </main>
</body>
</html>
```